Flyer-Design für Personalvermittlung
Zielgruppe
Wir machen Personalvermittlung (www.kraftwendel.de), Unternehmen, die einen eigenen Kunden haben sowie Unternehmen, die Kundenservice als Dienstleistung anbieten. DIe Zielgruppe sind Personalentscheider, Recruiter, HR-Direktoren, Kundenservicecenter-Leiter, Geschäftsführer). Weiterhin zählt zur Zielgruppe jeder wechselwillige Kandidat, der sich bei kraftwendel registrieren kann.
Aufgabenstellung
Ich hätte gerne ein zweiseitiges Flyerformat, was über Hostessen verteilbar ist, also nicht größer als A5. Inhalte können gerne aus der Homepage entnommen werden. Weiterhin in der Anlage ein Teaser, den wir Unternehmen zur Verfügung stellen. Vorderseite für Unternehmen, Rückseite für Kandidaten. Kernige Aussagen, wenig Text.

```html
<!DOCTYPE html>
<html lang="de">
<head>
<meta charset="utf-8">
<title>kraftwendel.de – Kandidaten</title>
<link href="https://fonts.googleapis.com/css2?family=Arimo:wght@400;700&display=swap" rel="stylesheet">
<style>
  :root {
    --teal: #7fc6b1;
    --navy: #1e2433;
    --ink: #1f2330;
    --paper: #ffffff;
    --footer-text: #c9ccd3;
  }
  * { margin: 0; padding: 0; box-sizing: border-box; }
  html, body { width: 846px; height: 1200px; overflow: hidden; background: var(--paper); }
  body { font-family: "Arimo", Arial, sans-serif; color: var(--ink); }
  .flyer { position: relative; width: 846px; height: 1200px; overflow: hidden; }

  .brand-mark { position: absolute; left: 339px; top: 20px; width: 168px; height: 168px; border-radius: 50%; background: var(--navy); }
  .brand-name { position: absolute; left: 521px; top: 84px; font-size: 27px; font-weight: 700; color: var(--navy); letter-spacing: 0.3px; }
  .brand-tagline { position: absolute; left: 522px; top: 118px; font-size: 12.5px; color: var(--navy); }

  .headline-band { position: absolute; left: 0; top: 221px; width: 846px; height: 49px; background: var(--teal);
    color: #fff; font-size: 26px; font-weight: 700; text-align: center; line-height: 49px; }

  .side-label { position: absolute; left: 0; top: 325px; width: 32px; height: 626px; background: var(--navy); }
  .side-label span { position: absolute; left: 16px; top: 54px; transform: translate(-50%, -50%) rotate(-90deg);
    color: #fff; font-size: 15px; font-weight: 700; letter-spacing: 0.5px; white-space: nowrap; }

  .audience { position: absolute; top: 325px; width: 210px; }
  .audience--agents { left: 86px; }
  .audience--specialists { left: 323px; }
  .audience--leaders { left: 559px; }
  .audience__photo { width: 201px; height: 133px; }
  .photo-agent { background: linear-gradient(135deg, #d9cfc3, #b9a89a 55%, #e6e0d8); }
  .photo-meeting { background: linear-gradient(135deg, #8c8e93, #e4e4e4 50%, #3a3a3e); }
  .photo-leader { background: linear-gradient(135deg, #d6d3cc, #3c4259 45%, #a9a499); }
  .audience__title { position: absolute; top: 146px; font-size: 16px; font-weight: 700; white-space: nowrap; }
  .audience--specialists .audience__title, .audience--specialists .audience__text { left: 4px; }
  .audience__text { position: absolute; top: 186px; width: 215px; font-size: 15.2px; line-height: 18.2px; }
  .audience__cta { position: absolute; width: 215px; font-size: 15.2px; line-height: 18.2px; }
  .audience--agents .audience__cta { top: 357px; }
  .audience--specialists .audience__cta { top: 375px; left: 4px; }
  .audience--leaders .audience__cta { top: 375px; }

  .benefit-bar { position: absolute; left: 86px; width: 673px; height: 35px; background: var(--teal);
    color: #fff; font-size: 15px; font-weight: 700; text-align: center; line-height: 35px; letter-spacing: 0.3px; }
  .benefit-bar--simple { top: 765px; }
  .benefit-bar--individual { top: 856px; }
  .benefit-text { position: absolute; left: 86px; width: 673px; text-align: center; font-size: 15.2px; line-height: 18.2px; }
  .benefit-text--simple { top: 808px; }
  .benefit-text--individual { top: 899px; }

  .call-to-action { position: absolute; left: 0; top: 993px; width: 846px; text-align: center;
    font-size: 27px; font-weight: 700; line-height: 29px; color: var(--navy); }

  .contact-footer { position: absolute; left: 0; top: 1071px; width: 846px; height: 129px; background: var(--navy); }
  .contact { position: absolute; top: 0; width: 160px; text-align: center; color: var(--footer-text); font-size: 11.5px; line-height: 15px; }
  .contact svg { position: absolute; top: 17px; left: 66px; width: 28px; height: 28px; }
  .contact__text { position: absolute; left: 0; width: 160px; top: 67px; }
  .contact--address .contact__text { top: 59px; }
  .contact--address { left: -3px; }
  .contact--web { left: 170px; }
  .contact--phone { left: 342px; }
  .contact--social { left: 516px; }
  .contact--mail { left: 688px; }
</style>
</head>
<body>
<main class="flyer">
  <header>
    <div class="brand-mark"></div>
    <div class="brand-name">kraftwendel.de</div>
    <div class="brand-tagline">Das Karriereportal im Kundenservice</div>
  </header>

  <h1 class="headline-band">Wir finden den richtigen Job für Ihre Karriere.</h1>

  <div class="side-label"><span>KANDIDATEN</span></div>

  <section class="audience audience--agents">
    <div class="audience__photo photo-agent" role="img" aria-label="Foto: Kundenservice-Mitarbeiterin mit Headset"></div>
    <h2 class="audience__title">FÜR AGENTEN</h2>
    <p class="audience__text">Sie sind Berufseinsteiger oder haben bereits Berufs-erfahrung im Kundenservice?<br>Als Kundenbetreuer oder Agent im Kundenservice macht Ihnen keiner etwas vor?</p>
    <p class="audience__cta">Dann melden Sie sich an und finden Sie Ihre berufliche Herausforderung!</p>
  </section>

  <section class="audience audience--specialists">
    <div class="audience__photo photo-meeting" role="img" aria-label="Foto: Gespräch am Schreibtisch mit Laptop und Kaffeetassen"></div>
    <h2 class="audience__title">FÜR SPEZIALISTEN</h2>
    <p class="audience__text">Sie kennen die operativen Abläufe im Kundenservice? Ihre Erfahrungen kommen aus dem WFM (Workforce Management), der Personaleinsatzplanung, dem Bereich Personal, der Buchhaltung, der IT oder dem Training?</p>
    <p class="audience__cta">Wir finden für Sie eine neue berufliche Perspektive!</p>
  </section>

  <section class="audience audience--leaders">
    <div class="audience__photo photo-leader" role="img" aria-label="Foto: Führungskraft mit Tablet vor einer Gruppe im Büro"></div>
    <h2 class="audience__title">FÜR FÜHRUNGSKRÄFTE</h2>
    <p class="audience__text">Sie haben bereits Führungserfahrung oder Sie suchen den nächsten Schritt als Team-, Projekt- oder Standortleiter, als Key Account Manager oder als Leiter einer Fachabteilung im Kundenservice?</p>
    <p class="audience__cta">Dann sind Sie hier genau richtig!</p>
  </section>

  <h3 class="benefit-bar benefit-bar--simple">EINFACH</h3>
  <p class="benefit-text benefit-text--simple">Ein Profil bei uns einzurichten dauert nur 5 Minuten. Falls noch Fragen offen sind,<br>melden wir uns umgehend bei Ihnen und besprechen die fehlenden Details.</p>

  <h3 class="benefit-bar benefit-bar--individual">INDIVIDUELL</h3>
  <p class="benefit-text benefit-text--individual">Wir sind Experten im Kundenservice und vermitteln Ihnen nur Jobangebote, die auch<br>wirklich zu Ihren individuellen Präferenzen passen. Sie entscheiden, wem wir zunächst<br>anonym und später personalisiert Ihre Daten zur Verfügung stellen.</p>

  <p class="call-to-action">Worauf warten Sie noch?<br>Jetzt anmelden und neuen Job finden!</p>

  <footer class="contact-footer">
    <div class="contact contact--address">
      <svg viewBox="0 0 28 28" fill="none" stroke="currentColor" stroke-width="1.6"><path d="M14 26c-5-6-9-10-9-15a9 9 0 0 1 18 0c0 5-4 9-9 15z"/><circle cx="14" cy="11" r="3.6"/></svg>
      <div class="contact__text">kraftwendel GmbH<br>Lindenhofweg 8<br>10247 Berlin</div>
    </div>
    <div class="contact contact--web">
      <svg viewBox="0 0 28 28" fill="none" stroke="currentColor" stroke-width="1.6"><path d="M3 14L14 4l11 10M6 11.5V25h6v-7h4v7h6V11.5"/></svg>
      <div class="contact__text">www.kraftwendel.de</div>
    </div>
    <div class="contact contact--phone">
      <svg viewBox="0 0 28 28" fill="none" stroke="currentColor" stroke-width="1.6"><circle cx="14" cy="14" r="12"/><path fill="currentColor" stroke="none" d="M9.5 8.5l2.3-.6 1.4 3-1.4 1.2c.7 1.6 1.9 2.9 3.5 3.6l1.2-1.4 3 1.4-.6 2.3c-5 .4-9.8-4.3-9.4-9.5z"/></svg>
      <div class="contact__text">49 [0]30 555 019 274</div>
    </div>
    <div class="contact contact--social">
      <svg viewBox="0 0 28 28" fill="none" stroke="currentColor" stroke-width="1.6"><circle cx="14" cy="14" r="12"/></svg>
      <div class="contact__text">kraftwendel_DE</div>
    </div>
    <div class="contact contact--mail">
      <svg viewBox="0 0 28 28" fill="none" stroke="currentColor" stroke-width="1.6"><rect x="2" y="6" width="24" height="17"/><path d="M2 6l12 10 12-10M2 23l9-8M26 23l-9-8"/></svg>
      <div class="contact__text">info@kraftwendel.de</div>
    </div>
  </footer>
</main>
</body>
</html>
```